photowall advertisement

We require a wall featuring our company logo. We would like to avoid the color green, and gold is highly preferred. The design should be similar to the one in the attached photo. The wall will be used for photos and promotional purposes during congresses. Files must be prepared for printing.
dimension of wall: 470x223 cm

Industry/Entity Type

lifestyle

Colors
0054AA
0677BA
7BADD7
CADEEF
E8F1F8
6B429C
8869AF
B7A5CE
E3DAEB
F3F0F8

Requirements
Must have
• gold color, white, and other compare with gold color
Nice to have
• some pictograms, maps of Europe

```html
<!DOCTYPE html>
<html lang="en">
<head>
<meta charset="utf-8">
<title>Aurel Tech – Photo Wall</title>
<link href="https://fonts.googleapis.com/css2?family=Michroma&display=swap" rel="stylesheet">
<style>
  :root {
    --wall-black: #111111;
    --mark-white: #ffffff;
    --brand-gold: #c39445;
  }
  html, body {
    margin: 0;
    padding: 0;
    width: 1200px;
    height: 569px;
    overflow: hidden;
    background: var(--wall-black);
  }
  .photo-wall {
    position: relative;
    width: 1200px;
    height: 569px;
    background: var(--wall-black);
    font-family: "Michroma", sans-serif;
  }
  .logo-row {
    position: absolute;
    display: flex;
    gap: 29px;
    transform: translateY(-50%);
  }
  .logo-row--full { left: 27px; }
  .logo-row--offset { left: 109px; }
  .logo-row--feature { left: 35px; gap: 112px; }

  .brand-lockup {
    display: flex;
    align-items: center;
    gap: 8px;
    width: 140px;
    color: var(--mark-white);
    font-size: 13px;
    letter-spacing: 0.5px;
    white-space: nowrap;
  }
  .brand-lockup__square {
    width: 14px;
    height: 14px;
    background: currentColor;
    flex: none;
  }
  .brand-lockup--feature {
    width: 300px;
    gap: 16px;
    color: var(--brand-gold);
    font-size: 29px;
    letter-spacing: 1px;
  }
  .brand-lockup--feature .brand-lockup__square {
    width: 34px;
    height: 34px;
  }
  .gold-rule {
    position: absolute;
    left: 0;
    top: 495px;
    width: 1200px;
    height: 3px;
    background: var(--brand-gold);
  }
  .skyline-band {
    position: absolute;
    left: 0;
    top: 512px;
    width: 1200px;
    height: 57px;
    background: linear-gradient(to bottom, rgba(195,148,69,0.55), var(--brand-gold));
  }
</style>
</head>
<body>
<main class="photo-wall">

  <div class="logo-row logo-row--full" style="top:30px">
    <div class="brand-lockup"><span class="brand-lockup__square"></span>AUREL TECH</div>
    <div class="brand-lockup"><span class="brand-lockup__square"></span>AUREL TECH</div>
    <div class="brand-lockup"><span class="brand-lockup__square"></span>AUREL TECH</div>
    <div class="brand-lockup"><span class="brand-lockup__square"></span>AUREL TECH</div>
    <div class="brand-lockup"><span class="brand-lockup__square"></span>AUREL TECH</div>
    <div class="brand-lockup"><span class="brand-lockup__square"></span>AUREL TECH</div>
    <div class="brand-lockup"><span class="brand-lockup__square"></span>AUREL TECH</div>
  </div>

  <div class="logo-row logo-row--offset" style="top:78px">
    <div class="brand-lockup"><span class="brand-lockup__square"></span>AUREL TECH</div>
    <div class="brand-lockup"><span class="brand-lockup__square"></span>AUREL TECH</div>
    <div class="brand-lockup"><span class="brand-lockup__square"></span>AUREL TECH</div>
    <div class="brand-lockup"><span class="brand-lockup__square"></span>AUREL TECH</div>
    <div class="brand-lockup"><span class="brand-lockup__square"></span>AUREL TECH</div>
    <div class="brand-lockup"><span class="brand-lockup__square"></span>AUREL TECH</div>
  </div>

  <div class="logo-row logo-row--full" style="top:126px">
    <div class="brand-lockup"><span class="brand-lockup__square"></span>AUREL TECH</div>
    <div class="brand-lockup"><span class="brand-lockup__square"></span>AUREL TECH</div>
    <div class="brand-lockup"><span class="brand-lockup__square"></span>AUREL TECH</div>
    <div class="brand-lockup"><span class="brand-lockup__square"></span>AUREL TECH</div>
    <div class="brand-lockup"><span class="brand-lockup__square"></span>AUREL TECH</div>
    <div class="brand-lockup"><span class="brand-lockup__square"></span>AUREL TECH</div>
    <div class="brand-lockup"><span class="brand-lockup__square"></span>AUREL TECH</div>
  </div>

  <div class="logo-row logo-row--feature" style="top:198px">
    <div class="brand-lockup brand-lockup--feature"><span class="brand-lockup__square"></span>AUREL TECH</div>
    <div class="brand-lockup brand-lockup--feature"><span class="brand-lockup__square"></span>AUREL TECH</div>
    <div class="brand-lockup brand-lockup--feature"><span class="brand-lockup__square"></span>AUREL TECH</div>
  </div>

  <div class="logo-row logo-row--full" style="top:273px">
    <div class="brand-lockup"><span class="brand-lockup__square"></span>AUREL TECH</div>
    <div class="brand-lockup"><span class="brand-lockup__square"></span>AUREL TECH</div>
    <div class="brand-lockup"><span class="brand-lockup__square"></span>AUREL TECH</div>
    <div class="brand-lockup"><span class="brand-lockup__square"></span>AUREL TECH</div>
    <div class="brand-lockup"><span class="brand-lockup__square"></span>AUREL TECH</div>
    <div class="brand-lockup"><span class="brand-lockup__square"></span>AUREL TECH</div>
    <div class="brand-lockup"><span class="brand-lockup__square"></span>AUREL TECH</div>
  </div>

  <div class="logo-row logo-row--offset" style="top:321px">
    <div class="brand-lockup"><span class="brand-lockup__square"></span>AUREL TECH</div>
    <div class="brand-lockup"><span class="brand-lockup__square"></span>AUREL TECH</div>
    <div class="brand-lockup"><span class="brand-lockup__square"></span>AUREL TECH</div>
    <div class="brand-lockup"><span class="brand-lockup__square"></span>AUREL TECH</div>
    <div class="brand-lockup"><span class="brand-lockup__square"></span>AUREL TECH</div>
    <div class="brand-lockup"><span class="brand-lockup__square"></span>AUREL TECH</div>
  </div>

  <div class="logo-row logo-row--full" style="top:369px">
    <div class="brand-lockup"><span class="brand-lockup__square"></span>AUREL TECH</div>
    <div class="brand-lockup"><span class="brand-lockup__square"></span>AUREL TECH</div>
    <div class="brand-lockup"><span class="brand-lockup__square"></span>AUREL TECH</div>
    <div class="brand-lockup"><span class="brand-lockup__square"></span>AUREL TECH</div>
    <div class="brand-lockup"><span class="brand-lockup__square"></span>AUREL TECH</div>
    <div class="brand-lockup"><span class="brand-lockup__square"></span>AUREL TECH</div>
    <div class="brand-lockup"><span class="brand-lockup__square"></span>AUREL TECH</div>
  </div>

  <div class="logo-row logo-row--offset" style="top:417px">
    <div class="brand-lockup"><span class="brand-lockup__square"></span>AUREL TECH</div>
    <div class="brand-lockup"><span class="brand-lockup__square"></span>AUREL TECH</div>
    <div class="brand-lockup"><span class="brand-lockup__square"></span>AUREL TECH</div>
    <div class="brand-lockup"><span class="brand-lockup__square"></span>AUREL TECH</div>
    <div class="brand-lockup"><span class="brand-lockup__square"></span>AUREL TECH</div>
    <div class="brand-lockup"><span class="brand-lockup__square"></span>AUREL TECH</div>
  </div>

  <div class="logo-row logo-row--full" style="top:464px">
    <div class="brand-lockup"><span class="brand-lockup__square"></span>AUREL TECH</div>
    <div class="brand-lockup"><span class="brand-lockup__square"></span>AUREL TECH</div>
    <div class="brand-lockup"><span class="brand-lockup__square"></span>AUREL TECH</div>
    <div class="brand-lockup"><span class="brand-lockup__square"></span>AUREL TECH</div>
    <div class="brand-lockup"><span class="brand-lockup__square"></span>AUREL TECH</div>
    <div class="brand-lockup"><span class="brand-lockup__square"></span>AUREL TECH</div>
    <div class="brand-lockup"><span class="brand-lockup__square"></span>AUREL TECH</div>
  </div>

  <div class="gold-rule"></div>
  <div class="skyline-band" role="img" aria-label="Gold silhouette skyline of European landmarks repeated across the bottom of the wall"></div>

</main>
</body>
</html>
```